Sole practitioner CPA needs stationery design work

I need design art work for stationery which I can take to my printer. I require letterhead, business card, with comp's slip ,envelope. I would also like a word template in the letterhead format, as well as an email signature.
There are some professional requirements regarding the Tallywise Institute motif, and the words "Liability limited by a scheme approved under Professional Standards legislation". I have attached a mock up letterhead which shows these items

Target Market(s)

Small business owners who will expect to see a professional image

Industry/Entity Type

Business

Requirements
Must have
• Must have TWI logo and the words "Liability limited by a scheme approved under Professional Standards Legislation".
Nice to have
• I have attached a 'sample" that has the logo and the words. But the sample scheme is not important.

```html
<!DOCTYPE html>
<html lang="en">
<head>
<meta charset="utf-8">
<title>Harlow Accounting Stationery</title>
<link href="https://fonts.googleapis.com/css2?family=Open+Sans:ital,wght@0,400;0,600;0,700;1,400&family=PT+Serif:ital@1&display=swap" rel="stylesheet">
<style>
  :root {
    --maroon: #7a2323;
    --orange: #f08a1c;
    --red-orange: #e4412a;
    --yellow: #f6d80c;
    --paper: #ffffff;
    --ink: #1c1c1c;
    --twi-blue: #1f4b8c;
    --backdrop: #e8e5e1;
    --window: #f4f4f4;
  }
  * { margin: 0; padding: 0; box-sizing: border-box; }
  html, body { width: 1200px; height: 835px; overflow: hidden; }
  body {
    background: var(--backdrop);
    font-family: "Open Sans", Arial, sans-serif;
    color: var(--ink);
    position: relative;
  }
  .sheet {
    position: absolute;
    background: var(--paper);
    overflow: hidden;
    box-shadow: 0 2px 8px rgba(0,0,0,.18);
  }
  .wave { position: absolute; left: 0; width: 100%; display: block; }
  .brand {
    position: absolute;
    text-align: left;
    color: #fff;
    display: flex;
    align-items: center;
    gap: 7px;
  }
  .brand-dot { border-radius: 50%; background: var(--orange); flex: none; }
  .brand-name { font-weight: 600; line-height: 1.1; display: block; }
  .brand-tagline { font-style: italic; display: block; line-height: 1.2; }
  .liability {
    position: absolute;
    font-family: "PT Serif", Georgia, serif;
    font-style: italic;
    color: var(--ink);
  }
  .contact {
    position: absolute;
    font-style: italic;
    line-height: 1.45;
    color: var(--ink);
  }
  .member {
    position: absolute;
    font-style: italic;
    line-height: 1.25;
    text-align: left;
  }
  .member-mark { display: flex; align-items: center; gap: 4px; margin-top: 4px; }
  .member-square { background: var(--twi-blue); flex: none; }
  .member-name { color: var(--twi-blue); font-style: normal; font-weight: 600; }

  /* letterhead */
  .letterhead { left: 49px; top: 80px; width: 493px; height: 706px; }
  .letterhead .wave { top: 0; height: 112px; }
  .letterhead .brand { right: 20px; top: 12px; }
  .letterhead .brand-dot { width: 30px; height: 30px; }
  .letterhead .brand-name { font-size: 15px; }
  .letterhead .brand-tagline { font-size: 9.5px; }
  .letterhead .liability { left: 0; right: 0; top: 647px; text-align: center; font-size: 10.5px; }
  .letterhead .contact { left: 22px; top: 670px; font-size: 7.5px; }
  .letterhead .member { right: 12px; top: 668px; font-size: 5.5px; }
  .letterhead .member-square { width: 9px; height: 9px; }
  .letterhead .member-name { font-size: 11px; }

  /* envelope */
  .envelope { left: 664px; top: 208px; width: 480px; height: 184px; overflow: visible; }
  .envelope-flap { position: absolute; left: 0; top: -60px; width: 480px; height: 61px; display: block; }
  .envelope .wave { top: 0; height: 112px; }
  .envelope .brand { right: 18px; top: 12px; }
  .envelope .brand-dot { width: 28px; height: 28px; }
  .envelope .brand-name { font-size: 14px; }
  .envelope .brand-tagline { font-size: 8.5px; }
  .envelope-window {
    position: absolute; left: 57px; top: 80px; width: 197px; height: 74px;
    border: 1px solid #e2e2e2; border-radius: 5px; background: var(--window);
  }
  .envelope .liability { left: 275px; top: 103px; font-size: 10px; line-height: 1.3; }
  .envelope .member { right: 10px; top: 148px; font-size: 4.5px; }
  .envelope .member-square { width: 8px; height: 8px; }
  .envelope .member-name { font-size: 10px; }

  /* business card */
  .card { left: 730px; top: 499px; width: 353px; height: 201px; }
  .card .wave { top: 0; height: 88px; }
  .card .brand { right: 12px; top: 9px; }
  .card .brand-dot { width: 26px; height: 26px; }
  .card .brand-name { font-size: 12.5px; }
  .card .brand-tagline { font-size: 7.5px; }
  .card .liability { left: 42px; top: 70px; font-size: 7px; }
  .card-name {
    position: absolute; left: 0; right: 0; top: 104px; text-align: center;
    font-size: 20px; font-weight: 700; letter-spacing: .5px;
  }
  .card .contact { left: 14px; top: 148px; font-size: 7.2px; }
  .card .member { right: 12px; top: 151px; font-size: 5px; }
  .card .member-square { width: 9px; height: 9px; }
  .card .member-name { font-size: 10.5px; }
</style>
</head>
<body>
  <svg width="0" height="0" style="position:absolute" aria-hidden="true">
    <defs>
      <linearGradient id="stripe" x1="0" x2="1" y1="0" y2="0">
        <stop offset="0" stop-color="#e4412a"/>
        <stop offset=".5" stop-color="#f39a1a"/>
        <stop offset="1" stop-color="#f6d80c"/>
      </linearGradient>
    </defs>
  </svg>

  <!-- Letterhead -->
  <section class="sheet letterhead">
    <svg class="wave" viewBox="0 0 500 120" preserveAspectRatio="none" aria-hidden="true">
      <path d="M0 0H500V58C380 55 210 48 95 60C45 66 12 86 0 104Z" fill="var(--maroon)"/>
      <path d="M0 104C12 86 45 66 95 60C210 48 380 55 500 58V64C380 61 210 56 100 66C50 71 15 90 0 113Z" fill="url(#stripe)"/>
    </svg>
    <div class="brand">
      <span class="brand-dot"></span>
      <span><span class="brand-name">harlow accounting</span><span class="brand-tagline">certified practicing accountant</span></span>
    </div>
    <p class="liability">“Liability limited by a scheme approved under Professional Standards Legislation”</p>
    <p class="contact">PO Box 418 Marrick&nbsp; WA&nbsp; 6390<br>0400 555 017<br>harlowaccounting@example.com<br>ABN&nbsp; 12 345 678 901</p>
    <div class="member">harlow accounting<br>is a TWI practice
      <div class="member-mark"><span class="member-square"></span><span class="member-name">TWI</span></div>
    </div>
  </section>

  <!-- Envelope -->
  <section class="sheet envelope">
    <svg class="envelope-flap" viewBox="0 0 480 61" preserveAspectRatio="none" aria-hidden="true">
      <path d="M0 61L12 0H466Q478 0 480 14V61Z" fill="var(--paper)"/>
    </svg>
    <svg class="wave" viewBox="0 0 500 120" preserveAspectRatio="none" aria-hidden="true">
      <path d="M0 0H500V57C380 54 210 47 95 60C45 66 12 88 0 108Z" fill="var(--maroon)"/>
      <path d="M0 108C12 88 45 66 95 60C210 47 380 54 500 57V63C380 60 210 55 100 66C50 71 15 93 0 117Z" fill="url(#stripe)"/>
    </svg>
    <div class="brand">
      <span class="brand-dot"></span>
      <span><span class="brand-name">harlow accounting</span><span class="brand-tagline">certified practicing accountant</span></span>
    </div>
    <div class="envelope-window"></div>
    <p class="liability">“Liability limited by a scheme approved<br>under Professional Standards Legislation”</p>
    <div class="member">harlow accounting<br>is a TWI practice
      <div class="member-mark"><span class="member-square"></span><span class="member-name">TWI</span></div>
    </div>
  </section>

  <!-- Business card -->
  <section class="sheet card">
    <svg class="wave" viewBox="0 0 500 120" preserveAspectRatio="none" aria-hidden="true">
      <path d="M0 0H500V72C380 68 210 60 95 76C45 84 12 104 0 112Z" fill="var(--maroon)"/>
      <path d="M0 112C12 104 45 84 95 76C210 60 380 68 500 72V79C380 75 210 70 100 84C50 90 15 110 0 120Z" fill="url(#stripe)"/>
    </svg>
    <div class="brand">
      <span class="brand-dot"></span>
      <span><span class="brand-name">harlow accounting</span><span class="brand-tagline">certified practicing accountant</span></span>
    </div>
    <p class="liability">“Liability limited by a scheme approved under Professional Standards Legislation”</p>
    <p class="card-name">HARLOW</p>
    <p class="contact">PO Box 418 Marrick&nbsp; WA&nbsp; 6390<br>0400 555 017<br>harlowaccounting@example.com<br>ABN&nbsp; 12 345 678 901</p>
    <div class="member">harlow accounting<br>is a TWI practice
      <div class="member-mark"><span class="member-square"></span><span class="member-name">TWI</span></div>
    </div>
  </section>
</body>
</html>
```